Business card design for a engineering company

I need a double sided business card design for my company "Verdmont Flow Solutions". The card will be used in Malaysia. Sleek and professional, with a little design flare to it.
Information to showcase:
1. Company logo
2. Name, title, phone, email address, website address
3. our products "Pumping technology, Valve & actuation, Air Moving Technology
Example:
Ravi Tanaka
Business manager
ravi.tanaka@verdmont-example.com
www.verdmont-example.com.my
- Pumping technology
- Valve & actuation
- Air moving technology
Target Market(s)
engineers, purchasing managers
Industry/Entity Type
Business
Contact Information for Business Card
Ravi Tanaka
Business manager
ravi.tanaka@verdmont-example.com
www.verdmont-example.com.my
- Pumping technology
- Valve & actuation
- Air moving technology
catch phrase : "Solving flow challenges, exceeding expectations"

```html
<!DOCTYPE html>
<html lang="en">
<head>
<meta charset="utf-8">
<title>Verdmont Flow Solutions – Business Card</title>
<link rel="stylesheet" href="https://fonts.googleapis.com/css2?family=Open+Sans:wght@400;600;700&display=swap">
<style>
  :root {
    --page: #ebe7e1;
    --navy-deep: #0c222c;
    --navy-light: #24485a;
    --orange: #f39a1e;
    --bullet-text: #a9b9c4;
    --ink: #17303c;
    --paper: #ffffff;
    --paper-shade: #e3e9ed;
    --rule: #2c4450;
  }
  * { box-sizing: border-box; margin: 0; padding: 0; }
  html, body {
    width: 1200px; height: 1163px; overflow: hidden;
    background: var(--page);
    font-family: "Open Sans", Arial, sans-serif;
  }
  .card {
    position: absolute; left: 227px; width: 746px; height: 426px;
    overflow: hidden;
    box-shadow: 0 3px 10px rgba(0,0,0,.18);
  }
  /* Front */
  .card-front {
    top: 138px;
    background: radial-gradient(ellipse at 100% 0%, var(--navy-light) 0%, var(--navy-deep) 75%);
  }
  .brand {
    position: absolute; display: flex; align-items: center; gap: 18px;
    color: var(--orange); font-weight: 600;
  }
  .brand-dot { border-radius: 50%; background: var(--orange); flex: none; }
  .brand-name { display: flex; flex-direction: column; line-height: 1; }
  .brand-main { letter-spacing: 1px; }
  .brand-sub { letter-spacing: 6px; margin-top: 8px; }
  .card-front .brand { right: 50px; top: 52px; }
  .card-front .brand-dot { width: 64px; height: 64px; }
  .card-front .brand-main { font-size: 52px; }
  .card-front .brand-sub { font-size: 19px; }

  .products {
    position: absolute; left: 53px; top: 225px; list-style: none;
  }
  .products li {
    display: flex; align-items: center; height: 44px;
    color: var(--bullet-text); font-size: 22px; font-weight: 600;
  }
  .products li::before {
    content: ""; width: 10px; height: 10px; border-radius: 50%;
    background: var(--orange); margin-right: 19px;
    box-shadow: 0 0 4px rgba(243,154,30,.6);
  }
  /* Back */
  .card-back {
    top: 598px;
    background: radial-gradient(ellipse at 20% 60%, var(--paper) 30%, var(--paper-shade) 100%);
  }
  .card-back .brand { left: 42px; top: 43px; }
  .card-back .brand-dot { width: 58px; height: 58px; }
  .card-back .brand-main { font-size: 46px; }
  .card-back .brand-sub { font-size: 17px; letter-spacing: 5px; }

  .name-row {
    position: absolute; left: 44px; right: 45px; top: 184px;
    display: flex; align-items: center;
  }
  .name-row .rule { height: 2px; background: var(--rule); }
  .name-row .rule-left { width: 321px; }
  .name-row .rule-right { flex: 1; }
  .person-name {
    color: var(--orange); font-size: 29px; font-weight: 700;
    padding: 0 10px;
  }
  .person-title {
    position: absolute; left: 374px; top: 227px;
    color: var(--ink); font-size: 22px; font-weight: 700;
  }
  .contact { position: absolute; left: 374px; top: 278px; list-style: none; }
  .contact li {
    display: flex; align-items: center; height: 45px;
    color: var(--ink); font-size: 19px;
  }
  .contact svg { width: 26px; height: 26px; margin-right: 23px; flex: none; }
  .card-band { position: absolute; left: 0; bottom: 0; width: 746px; height: 35px; }
</style>
</head>
<body>
  <section class="card card-front">
    <div class="brand">
      <span class="brand-dot"></span>
      <span class="brand-name"><span class="brand-main">VERDMONT</span><span class="brand-sub">FLOW SOLUTIONS</span></span>
    </div>
    <ul class="products">
      <li>Pumping technology</li>
      <li>Valve &amp; actuation</li>
      <li>Air moving technology</li>
    </ul>
  </section>

  <section class="card card-back">
    <div class="brand">
      <span class="brand-dot"></span>
      <span class="brand-name"><span class="brand-main">VERDMONT</span><span class="brand-sub">FLOW SOLUTIONS</span></span>
    </div>
    <div class="name-row">
      <span class="rule rule-left"></span>
      <span class="person-name">Ravi Tanaka</span>
      <span class="rule rule-right"></span>
    </div>
    <p class="person-title">Business manager</p>
    <ul class="contact">
      <li>
        <svg viewBox="0 0 26 26" aria-hidden="true">
          <path d="M2 9 L13 2 L24 9 V22 H2 Z" fill="#17303c"/>
          <path d="M5 9 H21 V15 L13 19 L5 15 Z" fill="#fff"/>
          <path d="M2 10 L13 17 L24 10" fill="none" stroke="#fff" stroke-width="1.5"/>
        </svg>
        ravi.tanaka@verdmont-example.com
      </li>
      <li>
        <svg viewBox="0 0 26 26" aria-hidden="true" fill="none" stroke="#17303c" stroke-width="1.8">
          <circle cx="13" cy="13" r="10.5"/>
          <ellipse cx="13" cy="13" rx="4.5" ry="10.5"/>
          <path d="M2.5 13 H23.5 M4.5 7.5 H21.5 M4.5 18.5 H21.5"/>
        </svg>
        www.verdmont-example.com.my
      </li>
    </ul>
    <svg class="card-band" viewBox="0 0 746 35" aria-hidden="true">
      <polygon points="0,0 151,0 139,35 0,35" fill="#f39a1e"/>
      <polygon points="160,0 746,0 746,35 148,35" fill="#0c222c"/>
    </svg>
  </section>
</body>
</html>
```